Medical Company in need of a Modern Flyer design for new Wound Care clinic.

Tri-Fold modern flyer design for our Woundcare company. Logo and description of services can be found on our website; https://www.birchline-woundcare.com/

```html
<!DOCTYPE html>
<html lang="en">
<head>
<meta charset="utf-8">
<title>Birchline Woundcare – Tri-Fold Flyer</title>
<link rel="stylesheet" href="https://fonts.googleapis.com/css2?family=Roboto:wght@500;700;900&display=swap">
<style>
:root{
  --ink-dark:#062b2b;
  --sand:#f6d4a1;
  --title:#333333;
  --white:#ffffff;
}
*{margin:0;padding:0;box-sizing:border-box}
html,body{width:1200px;height:927px;overflow:hidden;background:var(--ink-dark)}
body{font-family:"Roboto",Arial,sans-serif;font-weight:700;color:var(--white);position:relative}
.flyer{position:relative;width:1200px;height:927px;background:var(--ink-dark)}
.title-band{position:absolute;left:0;top:87px;width:1200px;height:203px;background:var(--sand)}
.panel-title{position:absolute;color:var(--title);font-weight:700;letter-spacing:.3px;white-space:nowrap}
.services-title{left:43px;top:210px;font-size:51px;line-height:60px}
.hbo-title{left:400px;width:400px;top:113px;text-align:center;font-size:50px;line-height:54px}
.priority-title{left:839px;top:160px;font-size:51px;line-height:54px}

.service-list{position:absolute;left:32px;top:301px;width:370px;list-style:none;font-size:17.5px;line-height:23.3px}
.service-list li{position:relative;padding-left:17px}
.service-list li::before{content:"";position:absolute;left:1px;top:8px;width:8px;height:8px;border-radius:50%;background:var(--white)}

.section-heading{position:absolute;font-size:40.5px;font-weight:700;line-height:46px;white-space:nowrap}
.types-heading{left:43px;top:474px}
.treatment-heading{left:400px;width:400px;top:478px;text-align:center}

.wound-types{position:absolute;left:32px;top:530px;font-size:13.2px;line-height:24px;font-weight:500;white-space:nowrap}
.wound-types span{display:inline-block;position:relative;padding-left:14px;margin-right:7px}
.wound-types span::before{content:"";position:absolute;left:0;top:9px;width:6px;height:6px;border-radius:50%;background:var(--white)}

.about-text{position:absolute;left:31px;top:685px;width:345px;font-size:12.8px;line-height:15.5px;font-weight:500}

.hbo-text{position:absolute;left:420px;width:360px;top:303px;text-align:center;font-size:17px;line-height:33px;white-space:nowrap}
.treatment-list{position:absolute;left:420px;width:360px;top:531px;text-align:center;font-size:12.6px;line-height:15.5px;white-space:nowrap}
.care-badge{position:absolute;left:476px;top:634px}

.value-heading{position:absolute;left:832px;font-size:27.5px;line-height:32px;white-space:nowrap}
.value-text{position:absolute;font-size:11px;line-height:14.5px;font-weight:500;white-space:nowrap}
.team{top:322px}
.facilities{top:388px}
.facilities-text{left:835px;top:434px}
.compassion{top:495px}
.compassion-text{left:843px;top:538px}

.plans-pill{position:absolute;left:852px;top:617px;width:296px;height:46px;border-radius:23px;background:var(--white);color:var(--title);font-size:26px;line-height:46px;text-align:center;white-space:nowrap}
.plans-text{position:absolute;left:850px;width:300px;top:687px;text-align:center;font-size:16.5px;line-height:22.9px;white-space:nowrap}
.plan-strip{position:absolute;left:800px;top:863px;width:400px;height:37px;background:var(--white);display:flex;align-items:center;justify-content:space-around;padding:0 6px}
.plan-name{color:var(--title);font-size:8.5px;font-weight:700;white-space:nowrap}
</style>
</head>
<body>
<main class="flyer">
  <div class="title-band"></div>
  <h1 class="panel-title services-title">Our Services</h1>
  <h1 class="panel-title hbo-title">Hyperbaric<br>Oxygen<br>Therapy</h1>
  <h1 class="panel-title priority-title">Your Health<br>is Our Priority</h1>

  <ul class="service-list">
    <li>Hyperbaric Oxygen Therapy (HBO):<br>A Cornerstone of Advanced Wound Care</li>
    <li>Debridement</li>
    <li>Advanced Wound Dressings</li>
    <li>Bio-engineered Skin Substitutes</li>
    <li>Compression Therapy and Edema<br>Management</li>
  </ul>

  <h2 class="section-heading types-heading">Wound Types</h2>
  <div class="wound-types">
    <span>Atypical Wounds</span><span>Bone Infections</span><span>Burn Wounds</span><br>
    <span>Chronic Wounds</span><span>Diabetic Ulcers</span><span>Diabetic Wounds</span><br>
    <span>Non-Healing Surgical Wounds</span><span>Infected Wounds</span><br>
    <span>Pilonidal Cysts</span><span>Surgical Wound Complications</span><br>
    <span>Venous Leg Ulcers</span><span>Pressure Ulcers</span><br>
    <span>Venous &amp; Arterial Ulcers</span>
  </div>

  <p class="about-text">At Birchline Woundcare we specialize in treating a wide range of complex and hard-to-heal wounds. Our expert team is equipped to care for atypical wounds, bone infections, burn wounds, chronic wounds, and diabetic ulcers. We also provide advanced care for non-healing surgical wounds, infected wounds, pilonidal cysts, pressure ulcers, and surgical wound complications. Additionally, we treat venous and arterial ulcers, including venous leg ulcers, using the latest techniques and personalized care plans to promote healing and prevent complications. No matter the wound type, our focus is on achieving optimal outcomes for every patient.</p>

  <p class="hbo-text">Hyperbaric oxygen therapy (HBO) helps<br>patients wounds heal faster by increasing<br>the normal amount of oxygen in the tissue<br>stimulating growth factor production and<br>reducing edema through vasoconstriction.</p>

  <h2 class="section-heading treatment-heading">Wound Treatment</h2>
  <p class="treatment-list">Compression Therapy Mechanical &amp; Enzymatic<br>Debridement Negative Pressure Wound Therapy<br>Post-Mohs Surgery Tissue Infection Management<br>Labs Total Contact Casting Wound Care Wound<br>Debridement</p>

  <svg class="care-badge" width="220" height="220" viewBox="0 0 220 220" aria-hidden="true">
    <circle cx="110" cy="109" r="109" fill="#ffffff"/>
    <polygon points="110,35 172,76 172,142 110,181 46,142 46,76" fill="#062b2b"/>
    <rect x="98" y="77" width="22" height="68" fill="#ffffff"/>
    <rect x="75" y="100" width="68" height="22" fill="#ffffff"/>
  </svg>

  <h3 class="value-heading team">(Meet Our Team)</h3>
  <h3 class="value-heading facilities">(State-of-the-Art Facilities)</h3>
  <p class="value-text facilities-text">Our clinic is equipped with the latest technology and modern<br>facilities to deliver advanced healthcare solutions.</p>
  <h3 class="value-heading compassion">(Compassionate Care)</h3>
  <p class="value-text compassion-text">We believe in providing compassionate care that focuses<br>on the holistic well-being of our patients.</p>

  <div class="plans-pill">Accepted Health Plans</div>
  <p class="plans-text">At My Site, we accept a variety of<br>health insurance plans to ensure<br>that you receive the care you need.<br>If your current plan is not listed,<br>please get in touch with us so we<br>can explore alternative options that<br>best suit your needs.</p>

  <div class="plan-strip">
    <span class="plan-name">Brevanta</span>
    <span class="plan-name">Norlux Plan</span>
    <span class="plan-name">Vellacor</span>
    <span class="plan-name">Quenmoor Health</span>
    <span class="plan-name">Talvique</span>
  </div>
</main>
</body>
</html>
```